Legal Agribusiness Capability Brochure Design

Design A4 sized 6 page Legal Agribusiness Capability Brochure. Design is to be consistent with current marketing materials - logo, letterhead, website and business card to be provided.
Cover page - Firm name and logo, Agribusiness Capability Statement heading with image 1 below
Inside cover page - About Us section with image 2 below then Awards section below image
Inside middle page - Our Expertise with image 3 below
Inside back page - Our Experience with image 4 below
Back page - Senior Lawyers with image 5 below
Outside Middle Back Page - Contact Us with image 6
Updates

To provide more details to designers for brochure

Target Market(s)

Agribusiness - Australia

Industry/Entity Type

Legal

Colors

Designer to choose colors to be used in the design.

Requirements
Must have
• Use content from uloaded file - Agribusiness Brochure Content
• Use images uploaded
• Professional appearance
• Consistent with current marketing and website https://ferngatelegal.com.au/

```html
<!DOCTYPE html>
<html lang="en">
<head>
<meta charset="utf-8">
<title>Ferngate Legal – Agribusiness Capability Statement</title>
<link href="https://fonts.googleapis.com/css2?family=Roboto:wght@300;400;500;700;900&display=swap" rel="stylesheet">
<style>
:root{
  --page-bg:#f2f2f2;
  --panel-light:#dce8f1;
  --panel-mid:#c8d7e0;
  --panel-right:#c6d5df;
  --brand-blue:#1f8bd0;
  --brand-grey:#5e6164;
  --text-dark:#3d4246;
  --text-grey:#55595d;
  --rule:#9aa3a9;
}
*{box-sizing:border-box;margin:0;padding:0}
html,body{width:1200px;height:750px;overflow:hidden}
body{background:var(--page-bg);font-family:"Roboto",sans-serif;color:var(--text-dark);position:relative}
.brochure{position:absolute;left:40px;top:104px;width:1120px;height:542px;display:flex;box-shadow:0 14px 24px rgba(0,0,0,.12)}
.panel{position:relative;height:100%;overflow:hidden}
.panel--contact{width:370px;background:var(--panel-light)}
.panel--lawyers{width:378px;background:var(--panel-mid)}
.panel--cover{width:372px;background:var(--panel-right)}

/* header */
.masthead{position:absolute;top:30px;left:0;width:100%;display:flex;align-items:center;justify-content:center;gap:10px}
.seal{width:40px;height:40px;border-radius:50%;background:#d8d8d8;border:2px solid #555}
.masthead .divider{width:1px;height:44px;background:var(--rule)}
.brand{display:flex;align-items:center;gap:7px}
.brand-square{width:16px;height:16px;background:var(--brand-blue)}
.brand-name{font-weight:700;font-size:19px;color:var(--brand-blue);letter-spacing:.3px;white-space:nowrap}
.award{width:40px;height:40px;border-radius:50%;background:#e6dcc0}

/* section heads */
.section-title{position:absolute;font-weight:400;font-size:12px;letter-spacing:1.4px;color:var(--text-grey);padding-bottom:3px;border-bottom:1px solid var(--rule)}

/* bands */
.band{position:absolute;top:209px;left:0;width:100%;height:11px}
.band svg{display:block}
.band-label{position:absolute;top:0;height:11px;line-height:11px;font-size:5.4px;font-weight:700;color:#fff;text-transform:uppercase;white-space:nowrap}
.band-label small{font-weight:400;font-size:4.8px}

.small-copy{font-size:4.6px;line-height:1.4;color:var(--text-dark)}

/* contact */
.contact-intro{position:absolute;left:94px;top:181px;width:200px;line-height:1.7}
.office{position:absolute;top:234px;width:112px}
.office--ridgeford{left:94px}
.office--perth{left:202px}
.office-row{display:flex;gap:6px;margin-bottom:5px;align-items:flex-start;line-height:1.7}
.office-row svg{flex:0 0 6px;margin-top:1px}
.office-link{color:var(--brand-blue);font-weight:700;letter-spacing:.3px}

/* lawyers */
.portrait{position:absolute;top:125px;height:83px;border-radius:2px}
.bio{position:absolute;top:229px}
.bio p{margin-bottom:2.5px}
.bio ul{list-style:none}
.bio--principal{left:40px;width:178px}
.bio--consultant{left:235px;width:102px}
.bio-divider{position:absolute;left:226px;top:229px;width:1px;height:100px;background:var(--rule)}

/* cover */
.cover-title{position:absolute;top:216px;left:0;width:100%;text-align:center;line-height:1}
.cover-title .kicker{display:block;font-weight:400;font-size:23px;color:var(--text-grey);letter-spacing:.5px;margin-bottom:5px}
.cover-title .headline{display:block;font-weight:900;font-size:29px;color:var(--brand-blue);letter-spacing:.4px;line-height:1.05}

/* image strip */
.image-strip{position:absolute;left:0;top:348px;width:100%;height:165px}
.strip-grey{position:absolute;left:0;top:0;width:42px;height:162px;background:var(--brand-grey)}
.strip-blue{position:absolute;right:0;top:0;width:40px;height:165px;background:var(--brand-blue)}
.photo-frame{position:absolute;left:40px;top:-2px;width:292px;height:170px;border-radius:46px 0 46px 0}
.panel--contact .photo-frame{background:var(--panel-light)}
.panel--lawyers .photo-frame{background:var(--panel-mid)}
.panel--cover .photo-frame{background:var(--panel-right)}
.photo{position:absolute;left:51px;top:0;width:270px;height:163px;border-radius:40px 0 40px 0}
.notch{position:absolute;left:174px;top:151px;width:0;height:0;border-left:10px solid transparent;border-right:10px solid transparent}
.panel--contact .notch{border-bottom:12px solid var(--panel-light)}
.panel--lawyers .notch{border-bottom:12px solid var(--panel-mid)}
.panel--cover .notch{border-bottom:12px solid var(--panel-right)}

.photo--harvest{background:linear-gradient(180deg,#c9bfb0 0%,#b7ab95 35%,#c9a35a 62%,#a9843f 100%)}
.photo--vineyard{background:linear-gradient(90deg,#7d3b30 0%,#8a5a3a 30%,#c7b79c 50%,#9a8a3e 70%,#6f7a38 100%)}
.photo--grazing{background:linear-gradient(180deg,#d9bd9a 0%,#cba37a 45%,#b07a4a 70%,#8e4f2a 100%)}
</style>
</head>
<body>
<main class="brochure">

  <section class="panel panel--contact">
    <header class="masthead">
      <div class="seal"></div><span class="divider"></span>
      <div class="brand"><span class="brand-square"></span><span class="brand-name">FERNGATE LEGAL</span></div>
      <span class="divider"></span><div class="award"></div>
    </header>

    <h2 class="section-title" style="left:94px;top:157px">CONTACT US</h2>
    <p class="contact-intro small-copy">If you have any questions or require any assistance in relation to agribusiness law, please contact us at our Ridgeford or Perth office.</p>

    <div class="band">
      <svg width="370" height="11" viewBox="0 0 370 11">
        <polygon points="0,0 191,0 197,5.5 191,11 0,11" fill="#5e6164"/>
        <polygon points="193,0 370,0 370,11 193,11 199,5.5" fill="#1f8bd0"/>
      </svg>
      <span class="band-label" style="left:94px">Ridgeford Office</span>
      <span class="band-label" style="left:218px">Perth Office</span>
    </div>

    <div class="office office--ridgeford small-copy">
      <div class="office-row">
        <svg width="6" height="8" viewBox="0 0 6 8"><path d="M3 0a3 3 0 0 1 3 3c0 2-3 5-3 5S0 5 0 3a3 3 0 0 1 3-3z" fill="#1f8bd0"/><circle cx="3" cy="3" r="1" fill="#dce8f1"/></svg>
        <span>Suite 2, Saltbush House<br>9 Saltbush Lane<br>Ridgeford WA 6590</span>
      </div>
      <div class="office-row">
        <svg width="6" height="6" viewBox="0 0 6 6"><path d="M1 0l1.2 1.6L1.5 2.5a4 4 0 0 0 2 2l.9-.7L6 5 5.2 6C2.5 6 0 3.5 0 .8z" fill="#1f8bd0"/></svg>
        <span>+61 8 9000 1240<br>+ 61 8 9000 1255</span>
      </div>
      <div class="office-row">
        <svg width="6" height="5" viewBox="0 0 6 5"><rect width="6" height="5" fill="#1f8bd0"/><path d="M0 0l3 2.5L6 0" stroke="#dce8f1" stroke-width=".6" fill="none"/></svg>
        <span>info@ferngatelegal.com.au</span>
      </div>
      <div class="office-row">
        <svg width="6" height="7" viewBox="0 0 6 7"><path d="M0 0l6 4-2.6.4L5 7l-1 .4-1.5-2.6L0 6z" fill="#1f8bd0"/></svg>
        <span class="office-link">https://ferngatelegal.com.au/</span>
      </div>
    </div>

    <div class="office office--perth small-copy">
      <div class="office-row">
        <svg width="6" height="8" viewBox="0 0 6 8"><path d="M3 0a3 3 0 0 1 3 3c0 2-3 5-3 5S0 5 0 3a3 3 0 0 1 3-3z" fill="#5e6164"/><circle cx="3" cy="3" r="1" fill="#dce8f1"/></svg>
        <span>18 Kestrel Avenue<br>West Perth WA 6080</span>
      </div>
      <div class="office-row">
        <svg width="6" height="6" viewBox="0 0 6 6"><path d="M1 0l1.2 1.6L1.5 2.5a4 4 0 0 0 2 2l.9-.7L6 5 5.2 6C2.5 6 0 3.5 0 .8z" fill="#5e6164"/></svg>
        <span>+61 8 9000 3350<br>+ 61 8 9000 3300</span>
      </div>
      <div class="office-row">
        <svg width="6" height="5" viewBox="0 0 6 5"><rect width="6" height="5" fill="#5e6164"/><path d="M0 0l3 2.5L6 0" stroke="#dce8f1" stroke-width=".6" fill="none"/></svg>
        <span>info@ferngatelegal.com.au</span>
      </div>
    </div>

    <div class="image-strip">
      <div class="strip-grey"></div><div class="strip-blue"></div>
      <div class="photo-frame"></div>
      <div class="photo photo--harvest" role="img" aria-label="Combine harvester cutting a golden wheat crop under a cloudy sky"></div>
      <div class="notch"></div>
    </div>
  </section>

  <section class="panel panel--lawyers">
    <header class="masthead">
      <div class="seal"></div><span class="divider"></span>
      <div class="brand"><span class="brand-square"></span><span class="brand-name">FERNGATE LEGAL</span></div>
      <span class="divider"></span><div class="award"></div>
    </header>

    <h2 class="section-title" style="left:0;right:0;margin:0 auto;width:118px;top:98px;text-align:center">SENIOR LAWYERS</h2>

    <div class="portrait" style="left:41px;width:81px;background:linear-gradient(180deg,#c8d7e0 0%,#b9c3c9 45%,#4d5257 100%)" role="img" aria-label="Portrait of principal lawyer in a grey suit"></div>
    <div class="portrait" style="left:236px;width:73px;background:linear-gradient(180deg,#c8d7e0 0%,#bcc4c9 45%,#2f3338 100%)" role="img" aria-label="Portrait of consultant lawyer in a dark suit"></div>

    <div class="band">
      <svg width="378" height="11" viewBox="0 0 378 11">
        <polygon points="0,0 221,0 227,5.5 221,11 0,11" fill="#5e6164"/>
        <polygon points="223,0 378,0 378,11 223,11 229,5.5" fill="#1f8bd0"/>
      </svg>
      <span class="band-label" style="left:40px">Tom Hartley, <small>Principal</small></span>
      <span class="band-label" style="left:235px">Mark Hartley, <small>Consultant</small></span>
    </div>

    <div class="bio bio--principal small-copy">
      <p>Tom has practiced exclusively as a commercial lawyer for over 20 years initially at Perth law firms and since 2009 in Ridgeford.</p>
      <p>In 2011, Tom established Ferngate Legal in Ridgeford and expanded with the opening of a Perth office in 2017.</p>
      <p>Tom has advised on a large number of commercial matters and disputes, particularly in relation to agribusiness, business, property, wills and estates. He has a proven track record of delivering results to clients, especially in relation to more complex commercial transactions and disputes.</p>
      <p>Tom has a specific interest in agribusiness, primarily due to his family being involved in agribusiness for several generations.</p>
      <p style="margin-bottom:1px">Ranked by Lex Rankings Guide as:</p>
      <ul>
        <li>• “Preeminent Agribusiness Lawyer – Western Australia, 2019” (Top 2 in W.A.)</li>
        <li>• “Leading Agribusiness Lawyer – Western Australia, 2018” (Top 5 in W.A.)</li>
        <li>• “Leading Agribusiness Lawyer – Western Australia, 2017” (Top 7 in W.A.)</li>
      </ul>
    </div>

    <span class="bio-divider"></span>

    <div class="bio bio--consultant small-copy">
      <p>Mark was awarded a Bachelor of Laws from the University of the West Coast in 1973. Since then Mark has been a partner at firms in Ridgeford and Harbourtown, as well as a principal of firms in Ridgeford and Harbourtown. In late 2009 Mark and his wife, Jen, made the decision to move back to Ridgeford where they had previously lived for approximately 11 years.</p>
      <p>Mark has accumulated experience in a wide range of areas in over 45 years of legal practice, particularly in relation to Agribusiness disputes and litigation, which is of great benefit to his clients.</p>
    </div>

    <div class="image-strip">
      <div class="strip-grey"></div><div class="strip-blue"></div>
      <div class="photo-frame"></div>
      <div class="photo photo--vineyard" role="img" aria-label="Rows of autumn grapevines either side of a dirt track"></div>
      <div class="notch"></div>
    </div>
  </section>

  <section class="panel panel--cover">
    <header class="masthead">
      <div class="seal"></div><span class="divider"></span>
      <div class="brand"><span class="brand-square"></span><span class="brand-name">FERNGATE LEGAL</span></div>
      <span class="divider"></span><div class="award"></div>
    </header>

    <h1 class="cover-title">
      <span class="kicker">AGRIBUSINESS</span>
      <span class="headline">CAPABILITY<br>STATEMENT</span>
    </h1>

    <div class="image-strip">
      <div class="strip-grey"></div><div class="strip-blue"></div>
      <div class="photo-frame"></div>
      <div class="photo photo--grazing" role="img" aria-label="Flock of sheep standing on dry red paddock land"></div>
      <div class="notch"></div>
    </div>
  </section>

</main>
</body>
</html>
```